Modern and Improved business card design for Family Dental Practice

We have 2 sets of logo we have designed and now just need a business card layout and design for the office. Colors are on the logo. We can choose which logo we want to go with . The font can be changed to whatever seems modern and relevant. We are family dental office that has been open for over 15 years in South Austin Texas.

Target Market(s)

Handout Business cards to referrals and specialists

Industry/Entity Type

Dental

Contact Information for Business Card

We need address, phone, website and email address. 4870 North Loop Rd Suite 208 , Austin,Texas 78651....phone: 512-480-7319.....email- info@maplebrookdental-example.com....website - MapleBrookDental-example.com

Font styles to use
Serif
Decorative

Requirements
Must have
• my logo. We have 2 logos, but we can use just one or if we can incorporate one on one side and the other on the other side.
Nice to have
• Really just need a modern look and clean that incorporates the logo and colors .

```html
<!DOCTYPE html>
<html lang="en">
<head>
<meta charset="utf-8">
<title>Maple Brook Family Dentistry – Business Card</title>
<link href="https://fonts.googleapis.com/css2?family=Didact+Gothic&display=swap" rel="stylesheet">
<style>
  :root {
    --page-bg: #e6e6e4;
    --card-white: #ffffff;
    --ink: #1d1d1b;
    --brand-green: #2f8a3c;
    --leaf-dark: #1f6b33;
    --leaf-mid: #5e9a3e;
    --leaf-light: #b7c46a;
    --leaf-pale: #eef0d8;
    --card-radius: 28px;
  }
  * { box-sizing: border-box; margin: 0; padding: 0; }
  html, body {
    width: 1200px; height: 900px; overflow: hidden;
    background: var(--page-bg);
    font-family: "Didact Gothic", "Century Gothic", sans-serif;
    color: var(--ink);
  }
  .canvas {
    width: 1200px; height: 900px;
    display: flex; align-items: center; justify-content: center; gap: 40px;
  }
  .card {
    position: relative;
    width: 540px; height: 310px;
    border-radius: var(--card-radius);
    overflow: hidden;
    box-shadow: 0 6px 18px rgba(0,0,0,0.12);
  }
  .card--front { background: var(--card-white); }

  .brand {
    display: flex; align-items: center; gap: 14px;
  }
  .brand__dot {
    width: 40px; height: 40px; border-radius: 50%;
    background: var(--brand-green); flex: none;
  }
  .brand__name {
    color: var(--brand-green);
    font-size: 26px; line-height: 1.05; letter-spacing: 0.5px;
    text-transform: uppercase;
  }
  .brand__name small { display: block; font-size: 13px; letter-spacing: 1px; margin-top: 6px; }

  .card--front .brand { position: absolute; left: 28px; top: 52px; }

  .contact-list {
    position: absolute; left: 28px; bottom: 40px;
    list-style: none; display: flex; flex-direction: column; gap: 8px;
    font-size: 13.5px;
  }
  .contact-list li { display: flex; align-items: center; gap: 8px; }
  .contact-icon { width: 14px; height: 14px; flex: none; }

  .card--back .artwork {
    position: absolute; inset: 0;
    background:
      radial-gradient(ellipse at 20% 40%, rgba(255,255,255,0.35), transparent 45%),
      linear-gradient(100deg, var(--leaf-dark) 0%, var(--leaf-mid) 35%, var(--leaf-light) 65%, var(--leaf-pale) 100%);
  }
  .card--back .brand { position: absolute; right: 30px; bottom: 48px; }
  .card--back .brand__dot { width: 34px; height: 34px; }
  .card--back .brand__name { font-size: 22px; }
  .card--back .brand__name small { font-size: 11px; }
</style>
</head>
<body>
<main class="canvas">
  <section class="card card--front" aria-label="Business card front">
    <div class="brand">
      <span class="brand__dot"></span>
      <p class="brand__name">Maple<br>Brook<small>Family Dentistry</small></p>
    </div>
    <ul class="contact-list">
      <li>
        <svg class="contact-icon" viewBox="0 0 16 16" aria-hidden="true"><circle cx="8" cy="8" r="7" fill="none" stroke="var(--brand-green)" stroke-width="1.5"/><path d="M8 4a2.5 2.5 0 0 0-2.5 2.5C5.5 8.5 8 12 8 12s2.5-3.5 2.5-5.5A2.5 2.5 0 0 0 8 4z" fill="var(--brand-green)"/></svg>
        4870 North Loop Rd Suite 208, Austin, Texas 78651
      </li>
      <li>
        <svg class="contact-icon" viewBox="0 0 16 16" aria-hidden="true"><circle cx="8" cy="8" r="7" fill="none" stroke="var(--brand-green)" stroke-width="1.5"/><path d="M5.5 4.5l1.5 0 .7 1.8-1 .8a5 5 0 0 0 2.2 2.2l.8-1 1.8.7v1.5a1 1 0 0 1-1 1A6 6 0 0 1 4.5 5.5a1 1 0 0 1 1-1z" fill="var(--brand-green)"/></svg>
        512-480-7319
      </li>
      <li>
        <svg class="contact-icon" viewBox="0 0 16 16" aria-hidden="true"><circle cx="8" cy="8" r="7" fill="none" stroke="var(--brand-green)" stroke-width="1.5"/><rect x="4.5" y="5.5" width="7" height="5" fill="none" stroke="var(--brand-green)" stroke-width="1.2"/><path d="M4.5 5.5L8 8.3l3.5-2.8" fill="none" stroke="var(--brand-green)" stroke-width="1.2"/></svg>
        info@maplebrookdental-example.com
      </li>
      <li>
        <svg class="contact-icon" viewBox="0 0 16 16" aria-hidden="true"><circle cx="8" cy="8" r="7" fill="none" stroke="var(--brand-green)" stroke-width="1.5"/><circle cx="8" cy="8" r="3.5" fill="none" stroke="var(--brand-green)" stroke-width="1.1"/><path d="M4.5 8h7M8 4.5v7" stroke="var(--brand-green)" stroke-width="1.1"/></svg>
        MapleBrookDental-example.com
      </li>
    </ul>
  </section>

  <section class="card card--back" aria-label="Business card back">
    <div class="artwork" role="img" aria-label="Abstract sweeping green leaf-like brush strokes fading into pale yellow-green"></div>
    <div class="brand">
      <span class="brand__dot"></span>
      <p class="brand__name">Maple<br>Brook<small>Family Dentistry</small></p>
    </div>
  </section>
</main>
</body>
</html>
```